Menu Design Project

We trying to replace old flyer/menu with some new design.
hello this is my old menu i attached in email and my logo, the text you can pick from the menu and and i also attached some new picture for the food ,with my menu size unfold. front and back and then fold to 3.5" * 11". please show me what best can you do .Trifold is fine but must have image of food,
this is indian Restaurant
thats fine to have trifold menu design do to short time

Need to add also food picture on menu

Font styles to use
Serif
Decorative
Script

Colors

Designer to choose colors to be used in the design.

Requirements
Must have
• food image on menu
• trifold is fine ( do to short time)
• menu has to elegant ,color or text can be optional, Menu need to be neat and clean no too much rush on between the words .

```html
<!DOCTYPE html>
<html lang="en">
<head>
<meta charset="utf-8">
<title>Saffron Court – Trifold Menu</title>
<link href="https://fonts.googleapis.com/css2?family=Arimo:wght@400;700&family=Tinos:wght@400;700&family=Marcellus&family=Pinyon+Script&display=swap" rel="stylesheet">
<style>
:root{
  --green:#57683a;
  --green-dark:#45552c;
  --green-light:#6b7c4a;
  --cream:#fbf5e2;
  --cream-deep:#f4e6b8;
  --price:#e9d58a;
  --ink:#1d1d1d;
  --white:#ffffff;
}
*{box-sizing:border-box;margin:0;padding:0}
html,body{width:1200px;height:1200px;overflow:hidden;background:#fff}
body{position:relative;font-family:"Tinos",serif;color:var(--white)}
.sheet{position:absolute}
.sheet-outside{left:235px;top:12px;width:760px;height:586px;background:var(--green)}
.sheet-inside{left:235px;top:610px;width:751px;height:580px;background:var(--green)}
.panel{position:absolute;top:0;bottom:0;display:flex;flex-direction:column}
.photo{position:relative;flex:none;display:flex;align-items:flex-end;justify-content:center}
.photo-title{font-family:"Arimo",sans-serif;font-weight:700;font-size:13px;color:var(--white);
  text-shadow:0 1px 2px rgba(0,0,0,.8),0 0 4px rgba(0,0,0,.6);padding-bottom:4px;letter-spacing:.2px}
.menu{list-style:none;flex:none;display:flex;flex-direction:column;justify-content:space-evenly;
  background:linear-gradient(90deg,var(--green-dark),var(--green) 40%,var(--green-light) 100%)}
.menu li{display:flex;justify-content:space-between;font-size:6.4px;text-transform:uppercase;line-height:1;letter-spacing:.2px}
.menu li span:last-child{color:var(--price);font-size:6px}
.menu-tight li{font-size:6px}
/* cover */
.cover{position:absolute;left:506px;top:8px;width:254px;height:578px;background:var(--cream);color:var(--ink);text-align:center;font-family:"Arimo",sans-serif}
.cover-band{position:absolute;left:0;right:0;bottom:0;height:22px;background:var(--green);color:var(--white);font-size:13.5px;line-height:22px}
.brand-mark{width:52px;height:52px;border:2px solid var(--ink);border-radius:50%;margin:30px auto 0}
.brand-name{font-family:"Marcellus",serif;font-size:21px;margin-top:22px}
.brand-sub{display:inline-block;background:var(--cream-deep);font-family:"Marcellus",serif;font-size:17px;padding:3px 8px;margin-top:4px;border-left:3px solid var(--green);border-right:3px solid var(--green)}
.tagline{font-family:"Pinyon Script",cursive;font-size:20px;font-weight:400;margin-top:10px;line-height:1}
.contact{font-size:9.6px;line-height:12.5px}
.service{display:inline-block;background:var(--cream-deep);font-weight:700;font-size:9px;line-height:9px;padding:2px 6px;margin-top:9px;text-transform:uppercase}
.hours{margin:12px 10px 0;border:1px solid #b9b19a;border-radius:10px;padding:5px 0}
.hours h3{font-family:"Tinos",serif;font-size:9.5px;text-transform:uppercase}
.hours p{font-size:8.6px;line-height:10.5px}
.lunch h3{font-family:"Tinos",serif;font-size:11px;margin-top:8px}
.lunch p{font-size:10px}
.interior{width:221px;height:146px;margin:9px auto 0;background:linear-gradient(180deg,#8a6a3c,#c7a46a 45%,#e2d2b0 75%,#b98e5c)}
.notes{font-size:10px;line-height:14px;margin-top:6px}
.notes .small{font-size:8.6px}
.contact-card{flex:1;background:var(--cream);color:var(--ink);text-align:center;font-family:"Arimo",sans-serif;padding-top:5px}
.contact-card .tagline{margin-top:0}
</style>
</head>
<body>

<!-- Outside of the trifold -->
<section class="sheet sheet-outside">
  <div class="panel" style="left:0;width:254px">
    <div class="photo" style="height:78px;margin-top:8px;background:linear-gradient(135deg,#e9cf94,#c98d45 55%,#6b3f1f)" role="img" aria-label="Photo of tandoori naan bread"><span class="photo-title">Tandoori bread</span></div>
    <ul class="menu" style="height:125px;padding:12px 20px 6px 44px">
      <li><span>Tandoori Roti</span><span>$1.75</span></li>
      <li><span>Tandoori Naan</span><span>$1.75</span></li>
      <li><span>Garlic Naan</span><span>$2.50</span></li>
      <li><span>Lachha Paratha</span><span>$2.50</span></li>
      <li><span>Onion Kulcha</span><span>$2.99</span></li>
      <li><span>Aloo Paratha</span><span>$2.99</span></li>
      <li><span>Gobhi Paratha</span><span>$3.50</span></li>
      <li><span>Pudina Paratha</span><span>$2.99</span></li>
      <li><span>Keema Naan</span><span>$3.99</span></li>
      <li><span>Jalebi Paratha</span><span>$2.99</span></li>
    </ul>
    <div class="photo" style="height:78px;background:radial-gradient(circle at 50% 40%,#e8a23c,#c26a1e 60%,#f2eee6 90%)" role="img" aria-label="Photo of a vegetarian curry in a bowl"><span class="photo-title">Handi Se (Vegetarian)</span></div>
    <ul class="menu menu-tight" style="height:212px;padding:6px 20px 4px 44px">
      <li><span>Paneer Makhni</span><span>$8.99</span></li>
      <li><span>Paneer Tikka Masala</span><span>$8.99</span></li>
      <li><span>Kadai Paneer</span><span>$8.99</span></li>
      <li><span>Palak Paneer</span><span>$8.99</span></li>
      <li><span>Mutter Paneer</span><span>$8.49</span></li>
      <li><span>Shahi Paneer</span><span>$8.99</span></li>
      <li><span>Paneer Bhurji</span><span>$10.99</span></li>
      <li><span>Malai Kofta</span><span>$8.99</span></li>
      <li><span>Navratan Korma</span><span>$8.99</span></li>
      <li><span>Kaju Mushroom Mutter</span><span>$9.29</span></li>
      <li><span>Methi Malai Mutter</span><span>$9.29</span></li>
      <li><span>Aloo Gobhi</span><span>$8.50</span></li>
      <li><span>Bhindi Masala</span><span>$8.50</span></li>
      <li><span>Achari Baigan</span><span>$8.49</span></li>
      <li><span>Baigan Bharta</span><span>$8.49</span></li>
      <li><span>Vegetable Jalfrezi</span><span>$8.49</span></li>
      <li><span>Zeera Aloo</span><span>$7.50</span></li>
      <li><span>Sarson Ka Saag</span><span>$8.49</span></li>
      <li><span>Chana Peshawari</span><span>$8.49</span></li>
      <li><span>Chana Palak</span><span>$8.49</span></li>
      <li><span>Punjabi Kadi</span><span>$8.49</span></li>
      <li><span>Daal Takar Yellow</span><span>$8.49</span></li>
      <li><span>Daal Tarka Black</span><span>$8.49</span></li>
      <li><span>Daal Makhni</span><span>$8.49</span></li>
    </ul>
    <div class="contact-card">
      <h2 class="tagline">The Best Indian Cuisine</h2>
      <p class="contact">240 Harbor Ave., Eastfield, NY 11500<br>Tel: 555-014-2200, 555-014-2201<br>Fax: 555-014-2209<br>E-mail: hello@saffroncourt.example</p>
    </div>
  </div>

  <div class="panel" style="left:254px;width:252px">
    <div class="photo" style="height:78px;margin-top:8px;background:radial-gradient(circle at 50% 45%,#f3efe6,#e3dccb 55%,#c9443d 85%)" role="img" aria-label="Photo of kheer rice pudding with almonds"><span class="photo-title">Desserts</span></div>
    <ul class="menu" style="height:78px;padding:10px 20px 6px 24px">
      <li><span>Kheer</span><span>$3.99</span></li>
      <li><span>Rasmalai (3 pc.)</span><span>$3.99</span></li>
      <li><span>Gajar Halwa</span><span>$3.99</span></li>
      <li><span>Gulab Jamun (3 pc.)</span><span>$3.99</span></li>
      <li><span>Ice Cream</span><span>$3.50</span></li>
    </ul>
    <div class="photo" style="height:76px;background:linear-gradient(90deg,#f6f4ef,#e07a2c 25%,#5a2418 45%,#f0a52a 65%,#f4c21e 85%,#f6f4ef)" role="img" aria-label="Photo of glasses of juice"><span class="photo-title">Beverages</span></div>
    <ul class="menu menu-tight" style="height:162px;padding:6px 20px 6px 20px">
      <li><span>Mango Lassi</span><span>$3.50</span></li>
      <li><span>Lassi (sweet or salted)</span><span>$3.50</span></li>
      <li><span>Fresh Lemonade</span><span>$2.99</span></li>
      <li><span>Pina Colada Virgin</span><span>$3.99</span></li>
      <li><span>Strawberry Daiquiri Virgin</span><span>$3.99</span></li>
      <li><span>Orange Juice</span><span>$2.99</span></li>
      <li><span>Pineapple Juice</span><span>$2.99</span></li>
      <li><span>Mango Juice</span><span>$2.99</span></li>
      <li><span>Masala Tea</span><span>$1.99</span></li>
      <li><span>Coffee</span><span></span></li>
      <li><span>Cold Beers</span><span></span></li>
      <li><span>(Domestic &amp; imported lagers and more...)</span><span></span></li>
      <li><span>Indian Beers</span><span></span></li>
      <li><span>Wines (750ml / 1.5 Ltr)</span><span>$22.00/$38.00</span></li>
      <li><span style="text-transform:none">Cola, Lemon-lime Soda, Ginger Ale</span><span>$1.50</span></li>
    </ul>
    <div class="photo" style="height:78px;background:radial-gradient(circle at 55% 40%,#e6c79a,#b7703c 55%,#7a3d22 85%)" role="img" aria-label="Photo of chicken biryani in a clay pot"><span class="photo-title">Briyani and Rice</span></div>
    <ul class="menu" style="flex:1;padding:8px 20px 6px 26px">
      <li><span>Chicken Biryani</span><span>$7.99</span></li>
      <li><span>Goat Biryani</span><span>$9.99</span></li>
      <li><span>Lamb Biryani</span><span>$9.99</span></li>
      <li><span>Shrimp Biryani</span><span>$10.99</span></li>
      <li><span>Vegetable Biryani</span><span>$7.99</span></li>
      <li><span>Zeera Rice</span><span>$3.99</span></li>
      <li><span>Peas Pulao</span><span>$5.99</span></li>
      <li><span>Royal Spl Biryani</span><span>$11.99</span></li>
    </ul>
  </div>

  <div class="cover">
    <div class="brand-mark" aria-hidden="true"></div>
    <h1 class="brand-name">Saffron Court</h1>
    <div class="brand-sub">Restaurant &amp; Banquet Hall</div>
    <h2 class="tagline">The Best Indian Cuisine</h2>
    <p class="contact">240 Harbor Ave., Eastfield, NY 11500<br>Tel: 555-014-2200, 555-014-2201<br>Fax: 555-014-2209<br>E-mail: hello@saffroncourt.example</p>
    <div class="service">Eat in Take out<br>Delivery &amp; Catering</div>
    <div class="hours">
      <h3>Business Hours</h3>
      <p>Sun - Thu: 11:30 AM - 12:00<br>Fri - Sat: 11:30 AM - 12:00</p>
      <div class="lunch"><h3>Lunch Special</h3><p>Mon - Sun: 11:30 Am - 4:00</p></div>
      <div class="interior" role="img" aria-label="Photo of the restaurant dining room"></div>
      <div class="notes">
        <p>WE DELIVER COLD BEER AND WINE</p>
        <p>Everthing made fresh to Open</p>
        <p class="small">WE ACCEPT ALL MAJOR CREDIT CARDS</p>
      </div>
    </div>
    <div class="cover-band">Visit us at www.saffroncourt.example</div>
  </div>
</section>

<!-- Inside of the trifold -->
<section class="sheet sheet-inside">
  <div class="panel" style="left:0;width:248px">
    <div class="photo" style="height:78px;margin-top:8px;background:linear-gradient(160deg,#d99a5c,#b0602c 50%,#e9e2d4)" role="img" aria-label="Photo of vegetable kebabs"><span class="photo-title">Vegeterian Appetizer</span></div>
    <ul class="menu" style="height:150px;padding:6px 22px 6px 26px">
      <li><span>Vegetable Samosa (2 pc.)</span><span>$2.99</span></li>
      <li><span>Samosa Chaat (2 pc.)</span><span>$7.99</span></li>
      <li><span>Aloo Tikki Chaat (4 pc.)</span><span>$6.99</span></li>
      <li><span>Mix Veg. Pakora</span><span>$6.50</span></li>
      <li><span>Papri Chaat</span><span>$6.50</span></li>
      <li><span>Dahi Bhalla</span><span>$6.99</span></li>
      <li><span>Paneer Pakora (7 pc.)</span><span>$8.95</span></li>
      <li><span>Vegetable Seekh Kabab</span><span>$11.99</span></li>
      <li><span>Panneer Tikka Tandoori</span><span>$8.99</span></li>
      <li><span>Stuffed Paneer Pakora (6 pc.)</span><span>$8.50</span></li>
      <li><span>Chatpati Aloo Chaat</span><span>$7.50</span></li>
    </ul>
    <div class="photo" style="height:80px;background:linear-gradient(90deg,#1d7fb8,#e8f3f6 35%,#2a62c8 55%,#f0a31f 80%,#e2382a)" role="img" aria-label="Photo of colourful cocktails"><span class="photo-title">Coctail</span></div>
    <ul class="menu" style="flex:1;padding:8px 22px 6px 26px">
      <li><span>Martini Coctail</span><span>$6.99</span></li>
      <li><span>Mojito Coctail</span><span>$8.99</span></li>
      <li><span>White Rum Coctail</span><span>$5.99</span></li>
      <li><span>Mai Tai Coctail</span><span>$4.99</span></li>
      <li><span>Bloody Mary</span><span>$9.99</span></li>
      <li><span>Daiquiri Coctail</span><span>$10.99</span></li>
      <li><span>Tropical Storm</span><span>$6.99</span></li>
      <li><span>Pina Colada</span><span>$6.99</span></li>
      <li><span>Tequila Blend</span><span>$6.99</span></li>
      <li><span>Banana D'Coctail</span><span>$6.99</span></li>
      <li><span>Cuban Rhum</span><span>$8.99</span></li>
      <li><span>Mango Daiquiri</span><span>$5.99</span></li>
      <li><span>Cuban Majito</span><span>$4.99</span></li>
      <li><span>Bloody Mary</span><span>$4.99</span></li>
      <li><span>Daiquiri Coctail</span><span>$10.99</span></li>
      <li><span>Maitai Coctail</span><span>$6.99</span></li>
      <li><span>Bloody Ma Coctail</span><span>$8.99</span></li>
      <li><span>Daiquiri Coctail</span><span>$5.99</span></li>
    </ul>
  </div>

  <div class="panel" style="left:248px;width:252px">
    <div class="photo" style="height:78px;margin-top:8px;background:radial-gradient(circle at 45% 45%,#c8432a,#8a1f16 55%,#3a5a22 90%)" role="img" aria-label="Photo of chilli chicken"><span class="photo-title">Indo chinese</span></div>
    <ul class="menu" style="height:122px;padding:4px 22px 6px 26px">
      <li><span>Chilli Paneer</span><span>$10.99</span></li>
      <li><span>Chilli Mushroom</span><span>$9.99</span></li>
      <li><span>Chilli Gobhi</span><span>$9.99</span></li>
      <li><span>Vegetable Manchurian</span><span>$9.50</span></li>
      <li><span>Vegetable Chowmin</span><span>$7.99</span></li>
      <li><span>Vegetable Spring Roll</span><span>$6.99</span></li>
      <li><span>Chilli Chicken</span><span>$10.99</span></li>
      <li><span>Chilli Fish</span><span>$11.99</span></li>
      <li><span>Chilli Shrimp</span><span>$12.99</span></li>
      <li><span>Chiken Manchurian</span><span>$10.99</span></li>
      <li><span>Chicken Chowmin</span><span>$9.99</span></li>
    </ul>
    <div class="photo" style="height:77px;background:radial-gradient(circle at 50% 45%,#d8361f,#9c1c12 60%,#5e7a3a 95%)" role="img" aria-label="Photo of tandoori chicken"><span class="photo-title">Non-Vegeterian Appetizer</span></div>
    <ul class="menu" style="flex:1;padding:8px 22px 8px 28px">
      <li><span>Chicken Samosa (2 pc.)</span><span>$5.99</span></li>
      <li><span>Chicken Pakora</span><span>$10.99</span></li>
      <li><span>Fish Amritsari</span><span>$11.99</span></li>
      <li><span>Tawa Chicken</span><span>$12.99</span></li>
      <li><span>Garlic Shrimp</span><span>$12.99</span></li>
      <li><span>Spicy Wings (8 pc.)</span><span>$8.99</span></li>
      <li><span>Tandoori Chicken</span><span>$8.99/12.99</span></li>
      <li><span>Lemon Chicken</span><span>$13.99</span></li>
      <li><span>Chicken Seekh Kabab</span><span>$9.50</span></li>
      <li><span>Lamb Seekh Kabab</span><span>$11.99</span></li>
      <li><span>Chicken Tikka</span><span>$10.50</span></li>
      <li><span>Chicken Malai Kabab</span><span>$10.99</span></li>
      <li><span>Achari Tikka</span><span>$10.99</span></li>
      <li><span>Afghani Chicken</span><span>$12.99</span></li>
      <li><span>Fish Tikka Tandoori</span><span>$11.99</span></li>
      <li><span>Salmon Fish</span><span>$13.50</span></li>
      <li><span>Tawa Fish</span><span>$12.99</span></li>
      <li><span>Tandoori Shrimp (6 pc.)</span><span>$14.99</span></li>
      <li><span>Lamb Chop (5 pc.)</span><span>$21.99</span></li>
      <li><span>Tandoori Mix Grill</span><span>$17.99</span></li>
    </ul>
  </div>

  <div class="panel" style="left:500px;width:251px">
    <div class="photo" style="height:70px;margin-top:8px;background:radial-gradient(circle at 50% 45%,#c8722a,#8a3a14 60%,#f1ece2 95%)" role="img" aria-label="Photo of chicken curry"><span class="photo-title">Handi Se (Non- Veg)</span></div>
    <ul class="menu menu-tight" style="height:185px;padding:3px 20px 3px 26px">
      <li><span>Chicken Makhni</span><span>$8.99</span></li>
      <li><span>Chicken Tikka Masala</span><span>$8.99</span></li>
      <li><span>Chicken Curry</span><span>$8.99</span></li>
      <li><span>Chicken Korma</span><span>$8.99</span></li>
      <li><span>Kadai Chicken</span><span>$8.99</span></li>
      <li><span>Chicken Saag</span><span>$8.99</span></li>
      <li><span>Chicken Jalfrezi</span><span>$8.99</span></li>
      <li><span>Chicken Masala</span><span>$8.99</span></li>
      <li><span>Chicken Vindaloo</span><span>$8.99</span></li>
      <li><span>Goat Curry</span><span>$9.99</span></li>
      <li><span>Goat Masala</span><span>$10.99</span></li>
      <li><span>Kadai Goat</span><span>$9.99</span></li>
      <li><span>Goat Saag</span><span>$9.99</span></li>
      <li><span>Goat Vindaloo</span><span>$9.99</span></li>
      <li><span>Chicken Keema Mutter</span><span>$10.99</span></li>
      <li><span>Lamb Curry</span><span>$10.99</span></li>
      <li><span>Lamb Rogan Josh</span><span>$10.99</span></li>
      <li><span>Lamb Saag</span><span>$10.99</span></li>
      <li><span>Lamb Korma</span><span>$10.99</span></li>
      <li><span>Lamb Bhuna Ghost</span><span>$10.99</span></li>
      <li><span>Lamb Vindaloo</span><span>$10.99</span></li>
      <li><span>Lamb Keema Mutter</span><span>$12.99</span></li>
    </ul>
    <div class="photo" style="height:70px;background:radial-gradient(circle at 55% 45%,#eef0e6,#d6d9cb 55%,#8a9a70 95%)" role="img" aria-label="Photo of raita garnished with mint"><span class="photo-title">Soup, Salad &amp; Raita</span></div>
    <ul class="menu menu-tight" style="height:88px;padding:4px 20px 4px 26px">
      <li><span>Tomato Soup</span><span>$3.99</span></li>
      <li><span>Vegetarian Soup</span><span>$3.99</span></li>
      <li><span>Chicken Soup</span><span>$4.50</span></li>
      <li><span>Hot N Sour Soup (chicken or veg)</span><span>$4.99</span></li>
      <li><span>Fresh Garden Salad</span><span>$4.50</span></li>
      <li><span>Masala Salad (house special)</span><span>$5.99</span></li>
      <li><span>Mix Raita</span><span>$3.99</span></li>
      <li><span>Boondi Raita</span><span>$3.99</span></li>
      <li><span>Pudina Raita</span><span>$3.99</span></li>
      <li><span>Plain Dahi</span><span>$3.50</span></li>
    </ul>
    <div class="photo" style="height:64px;background:radial-gradient(circle at 50% 45%,#e08a2a,#b5401a 60%,#f1ece2 95%)" role="img" aria-label="Photo of fish curry"><span class="photo-title">Sea Food Special</span></div>
    <ul class="menu menu-tight" style="flex:1;padding:3px 20px 3px 26px">
      <li><span>Kadai Fish</span><span>$13.99</span></li>
      <li><span>Fish Curry</span><span>$13.99</span></li>
      <li><span>Fish Masala</span><span>$13.99</span></li>
      <li><span>Goa Fish Curry</span><span>$12.59</span></li>
      <li><span>Fish Tikka Masala</span><span>$12.59</span></li>
      <li><span>Shrimp Curry</span><span>$12.99</span></li>
      <li><span>Shrimp Masala</span><span>$12.99</span></li>
      <li><span>Shrimp Saag</span><span>$12.99</span></li>
      <li><span>Shrimp Bhuna</span><span>$12.99</span></li>
      <li><span>Shrimp Vindaloo</span><span>$12.99</span></li>
      <li><span>Kadai Shrimp</span><span>$12.99</span></li>
    </ul>
  </div>
</section>

</body>
</html>
```